Home care agency

Current website QRVCAREPLUS.com. Need to update and reformat to different pages. use my info from my current website

Target Market(s)

adult children

Industry/Entity Type

Home Health

Coding

Coded - Design and coding required

Number of Pages Required

4 page

Font styles to use
Sans Serif

Colors
3276b5
33a6d7
3277b5
85cae6
85acd3

```html
<!DOCTYPE html>
<html lang="en">
<head>
<meta charset="utf-8">
<title>Quarry Vale Care Plus</title>
<link href="https://fonts.googleapis.com/css2?family=Open+Sans:wght@400;600;700&family=Ubuntu:wght@500;700&display=swap" rel="stylesheet">
<style>
:root{
  --blue:#3276b5;
  --blue-bright:#33a6d7;
  --blue-soft:#85acd3;
  --sky:#85cae6;
  --map:#c9dbec;
  --ink:#111;
  --text:#333;
  --white:#fff;
}
*{box-sizing:border-box;margin:0;padding:0}
html,body{width:1200px;height:3730px;overflow:hidden;background:#fff}
body{font-family:"Open Sans",sans-serif;color:var(--text)}
.canvas{position:relative;width:1200px;height:3730px;overflow:hidden}
.abs{position:absolute}

.topbar{left:0;top:0;width:1200px;height:29px;background:var(--blue);color:#fff;font-size:10px}
.topbar .tagline{position:absolute;left:224px;top:8px}
.topbar .meta{position:absolute;right:226px;top:8px;display:flex;gap:16px}

.brand{left:224px;top:60px;width:124px;text-align:center;font-family:"Ubuntu",sans-serif;font-weight:500;color:var(--blue-soft);font-size:15px;line-height:19px}
.nav{left:562px;top:96px;display:flex;gap:18px;font-family:"Ubuntu",sans-serif;font-weight:500;font-size:15px;color:var(--blue)}
.nav .active{border-bottom:2px solid var(--blue);padding-bottom:2px}
.search{left:956px;top:97px}

.hero{left:0;top:185px;width:1200px;height:481px;background:linear-gradient(100deg,#6d9bcf 0%,#5a8dc6 45%,#4f85c0 100%);clip-path:polygon(0 0,100% 0,100% 100%,0 88%)}
.hero-text{left:0;top:300px;width:1200px;text-align:center;color:#fff;font-family:"Ubuntu",sans-serif;font-weight:700;text-shadow:0 2px 6px rgba(0,0,0,.25)}
.hero-text .small{font-size:44px;line-height:60px}
.hero-text .big{font-size:58px;line-height:68px}
.hero-btn{left:495px;top:510px;width:210px;height:50px;border:2px solid #fff;border-radius:14px;color:#fff;font-family:"Ubuntu",sans-serif;font-weight:500;font-size:26px;text-align:center;line-height:46px}

.section-title{left:0;width:1200px;text-align:center;font-family:"Ubuntu",sans-serif;font-weight:500;font-size:32px;color:var(--blue)}
.chevron{left:588px}

.portrait{left:224px;top:822px;width:317px;height:301px;background:linear-gradient(160deg,#e9e6e1 0%,#b8aca2 55%,#5c4b52 100%)}
.about-copy{left:612px;top:828px;width:363px;font-size:13px;line-height:16px;text-align:justify;color:var(--text)}
.about-copy p+p{margin-top:16px}

.map{left:0;top:1293px;width:1200px;height:1171px;background:linear-gradient(180deg,#c3d6ea,#cddff0)}
.card{position:absolute;width:351px;height:327px;background:var(--blue);color:#fff;box-shadow:0 4px 12px rgba(0,0,0,.28);text-align:center;padding:42px 24px 0;overflow:hidden}
.card.light{background:#fff;color:var(--ink);padding-top:20px}
.card .icon{display:block;margin:0 auto}
.card h3{font-family:"Ubuntu",sans-serif;font-weight:500;font-size:23px;line-height:28px;margin:22px 0 18px}
.card.light h3{text-transform:uppercase;letter-spacing:.3px;margin:18px 0 12px}
.card p{font-size:12.5px;line-height:15px;margin:0 24px 14px}
.card ul{list-style:none;font-size:12.5px;line-height:29.6px}

.contact-col{position:absolute;top:2640px;width:230px;text-align:center}
.contact-col h4{font-family:"Ubuntu",sans-serif;font-weight:500;font-size:21px;color:var(--ink);margin:12px 0 12px}
.contact-col p{font-size:11px;line-height:13px;color:var(--text)}
.contact-col strong{font-weight:600;color:var(--ink)}

.form-band{left:0;top:2957px;width:1200px;height:672px;background:linear-gradient(110deg,#4d82bd 0%,#3f76b3 50%,#4a7fba 100%)}
.form{color:#fff;font-family:"Ubuntu",sans-serif;font-weight:500}
.form .head{position:absolute;font-size:22px;border-bottom:2px solid #fff;padding-bottom:1px}
.form .head.sm{font-size:19px}
.form label{position:absolute;font-size:18px;white-space:nowrap}
.form label.sm{font-size:16px}
.field{position:absolute;background:#fff;border:1px solid #ccc;font-family:"Open Sans",sans-serif;font-size:12px;color:#999;padding-left:12px;display:flex;align-items:center}
.field.sm{font-size:10px;padding-left:10px}
.field.c{justify-content:center;padding-left:0}
.radios{position:absolute;left:246px;top:3383px;display:flex;gap:34px;font-family:"Open Sans",sans-serif;font-size:12px;color:#dfe9f5}
.radios span::before{content:"";display:inline-block;width:6px;height:6px;border-radius:50%;background:#fff;margin-right:6px;vertical-align:middle}
.note{position:absolute;left:228px;top:3446px;width:330px;font-family:"Open Sans",sans-serif;font-weight:600;font-size:12px;line-height:15px}
.submit{position:absolute;left:473px;top:3577px;width:154px;height:25px;background:var(--blue);color:#fff;font-family:"Open Sans",sans-serif;font-weight:700;font-size:13px;text-align:center;line-height:25px}

.footer{left:0;top:3629px;width:1200px;height:101px;background:#000}
.social{position:absolute;left:526px;top:3661px;display:flex;gap:15px}
.social span{width:17px;height:17px;border-radius:3px;background:#9aa3ad}
.copyright{position:absolute;left:0;top:3694px;width:1200px;text-align:center;color:#fff;font-size:10px}
</style>
</head>
<body>
<div class="canvas">

  <div class="abs topbar">
    <span class="tagline">Providing Care Throughout the Bay Coast</span>
    <span class="meta"><span>&#9742; 555-010-4477</span><span>&#9679; Login</span></span>
  </div>

  <div class="abs brand">Quarry Vale<br>Care Plus</div>
  <nav class="abs nav">
    <span class="active">About Us</span><span>Services</span><span>Contact</span><span>Care Inquiry Form</span>
  </nav>
  <svg class="abs search" width="18" height="18" viewBox="0 0 18 18" fill="none" stroke="#3276b5" stroke-width="2.2"><circle cx="7.5" cy="7.5" r="5.5"/><path d="M11.5 11.5l5 5"/></svg>

  <div class="abs hero" role="img" aria-label="Nurse with clipboard smiling at an older patient in a hospital bed, in blue tones"></div>
  <div class="abs hero-text">
    <div class="small">Welcome to the</div>
    <div class="big">Quarry Vale<br>Care Plus</div>
  </div>
  <div class="abs hero-btn">Read more</div>

  <h2 class="abs section-title" style="top:720px">About Us</h2>
  <svg class="abs chevron" style="top:766px" width="24" height="14" viewBox="0 0 24 14" fill="none" stroke="#3276b5" stroke-width="3.5"><path d="M2 2l10 9 10-9"/></svg>

  <div class="abs portrait" role="img" aria-label="Portrait of the founder, a nurse in a white coat seated in a chair"></div>
  <div class="abs about-copy">
    <p>Quarry Vale Care Plus is owned and operated by Dana Whitcomb. Dana is a registered nurse and has been in the health care system since 2001. She has specialized in home care, cardiology, trauma and critical care. She invests in future caregivers and has taught for the nursing programs at Harborview University, Coastal Health Institute, and Bayside College.</p>
    <p>All Quarry Vale caregivers have extensive background checks and training regarding HIPAA compliance. We individualize the care of our clients in order to provide the best care possible in their home. Quarry Vale also ensures full access and understanding of client care at all times with a caregiver binder in the client's home at all times. This binder includes information on the client's care plan along and the notes from their caregivers. This will allow all caregivers and the client's family to have an understanding of the care being provided.</p>
  </div>

  <h2 class="abs section-title" style="top:1188px">Services</h2>
  <svg class="abs chevron" style="top:1233px" width="24" height="14" viewBox="0 0 24 14" fill="none" stroke="#3276b5" stroke-width="3.5"><path d="M2 2l10 9 10-9"/></svg>

  <div class="abs map" role="img" aria-label="Faded map of towns in the service region"></div>

  <div class="card" style="left:224px;top:1362px">
    <svg class="icon" width="52" height="52" viewBox="0 0 52 52"><circle cx="26" cy="26" r="26" fill="#fff"/><circle cx="26" cy="20" r="7" fill="#000"/><path d="M13 38c0-8 6-11 13-11s13 3 13 11z" fill="#000"/></svg>
    <h3>Why Choose Home Care?</h3>
    <p>Home care is a cost-effective option that allows clients the ability to receive one-on-one care in the comfort of their own home.</p>
    <p>Home care also provides peace of mind to a client's family, near or far, without taking away a client's independence or privacy.</p>
  </div>
  <div class="card" style="left:624px;top:1362px">
    <svg class="icon" width="52" height="52" viewBox="0 0 52 52"><circle cx="26" cy="26" r="26" fill="#fff"/><circle cx="26" cy="20" r="7" fill="#000"/><path d="M13 38c0-8 6-11 13-11s13 3 13 11z" fill="#000"/></svg>
    <h3>Care Schedule/Frequency</h3>
    <p>Quarry Vale non-medical visits require a four hour minimum visit.</p>
    <p>There are no weekly minimum for medical or non-medical visits.</p>
    <p>Clients needing 24-hour care can save up 30% off of services by using a live-in caregiver. (Live-in caregiver requires personal bedroom and bathroom.)</p>
  </div>

  <div class="card light" style="left:224px;top:1721px">
    <svg class="icon" width="52" height="52" viewBox="0 0 52 52"><circle cx="26" cy="26" r="26" fill="#000"/><circle cx="26" cy="20" r="7" fill="#fff"/><path d="M13 38c0-8 6-11 13-11s13 3 13 11z" fill="#fff"/></svg>
    <h3>Skilled Care Services</h3>
    <ul><li>Free Initial Nursing Assessment</li><li>Wound Care</li><li>Injections</li><li>Medical Care Assistance</li><li>Transportation to Medical Appointments</li><li>Care Plan Management</li></ul>
  </div>
  <div class="card light" style="left:624px;top:1721px">
    <svg class="icon" width="52" height="52" viewBox="0 0 52 52"><circle cx="26" cy="26" r="26" fill="#000"/><circle cx="26" cy="20" r="7" fill="#fff"/><path d="M13 38c0-8 6-11 13-11s13 3 13 11z" fill="#fff"/></svg>
    <h3>Non-Medical Services</h3>
    <ul><li>Live-In Care</li><li>Respite Care</li><li>Assisting with Daily Living Activities</li><li>Meal Preparations</li><li>Companionship</li><li>Homemaking</li></ul>
  </div>

  <div class="card" style="left:224px;top:2083px">
    <svg class="icon" width="52" height="52" viewBox="0 0 52 52"><circle cx="26" cy="26" r="26" fill="#fff"/><circle cx="26" cy="20" r="7" fill="#000"/><path d="M13 38c0-8 6-11 13-11s13 3 13 11z" fill="#000"/></svg>
    <h3>CLIENT BENEFITS</h3>
    <p>Continuity of care with same caregiver for each client on a regular basis.</p>
    <p>Open communication with owner by phone or email.</p>
    <p>Ongoing communications to client's family by phone or email on a weekly basis (if desired.)</p>
    <p>Streamlined payment process.</p>
  </div>
  <div class="card" style="left:624px;top:2083px">
    <svg class="icon" width="52" height="52" viewBox="0 0 52 52"><circle cx="26" cy="26" r="26" fill="#fff"/><circle cx="26" cy="20" r="7" fill="#000"/><path d="M13 38c0-8 6-11 13-11s13 3 13 11z" fill="#000"/></svg>
    <h3>Payment Options</h3>
    <p>Quarry Vale currently accepts check for service payments (with plans for online payments late 2018.)</p>
    <p>Quarry Vale currently accepts check for service payments (with plans for online payments late 2018.)</p>
    <p>Quarry Vale currently accepts check for service payments (with plans for online payments late 2018.)</p>
  </div>

  <h2 class="abs section-title" style="top:2523px">Contact</h2>
  <svg class="abs chevron" style="top:2570px" width="24" height="14" viewBox="0 0 24 14" fill="none" stroke="#3276b5" stroke-width="3.5"><path d="M2 2l10 9 10-9"/></svg>

  <div class="contact-col" style="left:218px">
    <svg width="48" height="48" viewBox="0 0 48 48"><circle cx="24" cy="24" r="24" fill="#3276b5"/><circle cx="24" cy="18" r="6.5" fill="#fff"/><path d="M12 35c0-7 5-10 12-10s12 3 12 10z" fill="#fff"/></svg>
    <h4>Contact Online</h4>
    <p>To contact us online, please fill out the care inquiry form below and you will be contacted within 24-48 hours.</p>
  </div>
  <div class="contact-col" style="left:496px">
    <svg width="48" height="48" viewBox="0 0 48 48"><circle cx="24" cy="24" r="24" fill="#3276b5"/><path d="M17 14c1.5-1 3-.8 3.8.6l2 3.4c.6 1.1.3 2.2-.7 2.9l-1.2.8c1 2.4 2.9 4.4 5.3 5.5l.9-1.2c.7-.9 1.900-1.2 2.9-.6l3.3 2.1c1.3.8 1.5 2.4.5 3.8-1.4 2-3.6 2.6-6 1.6-5.6-2.4-10-6.9-12.2-12.5-.9-2.4-.3-4.7 1.4-6.4z" fill="#fff"/></svg>
    <h4>Contact By Phone</h4>
    <p>If you would like to speak with someone over the phone about your care inquiry, you can contact Quarry Vale Monday-Friday 9:00am-5:00pm at 555-010-4477.</p>
  </div>
  <div class="contact-col" style="left:766px">
    <svg width="48" height="48" viewBox="0 0 48 48"><circle cx="24" cy="24" r="24" fill="#3276b5"/><rect x="12" y="16" width="24" height="17" rx="1.5" fill="#fff"/><path d="M12.5 17l11.5 9 11.5-9" fill="none" stroke="#3276b5" stroke-width="1.8"/></svg>
    <h4>Mailing Address</h4>
    <p>Please mail all service payments and employment applications to:<br><br><strong>Quarry Vale Care Plus<br>PO Box 12 Seabrook, ST 00000</strong></p>
  </div>

  <h2 class="abs section-title" style="top:2869px">Care Inquiry Form</h2>
  <svg class="abs chevron" style="top:2916px" width="24" height="14" viewBox="0 0 24 14" fill="none" stroke="#3276b5" stroke-width="3.5"><path d="M2 2l10 9 10-9"/></svg>

  <div class="abs form-band" role="img" aria-label="Caregiver visiting a client at home, tinted blue"></div>

  <div class="form">
    <div class="head" style="left:224px;top:2988px">Contact Information</div>
    <label style="left:224px;top:3038px">Contact Name *</label>
    <div class="field" style="left:224px;top:3070px;width:226px;height:32px">First Name</div>
    <label style="left:224px;top:3116px">Last Name</label>
    <div class="field" style="left:224px;top:3148px;width:226px;height:32px">Last Name</div>
    <label style="left:224px;top:3191px">Contact Email Address *</label>
    <div class="field" style="left:224px;top:3224px;width:226px;height:32px">Email Address</div>
    <label style="left:224px;top:3272px">Contact Phone Number *</label>
    <div class="field c" style="left:224px;top:3305px;width:68px;height:32px">(###)</div>
    <div class="field c" style="left:300px;top:3305px;width:68px;height:32px">###</div>
    <div class="field c" style="left:375px;top:3305px;width:68px;height:32px">####</div>
    <label style="left:224px;top:3353px">Best Way to Reach You *</label>
    <div class="radios"><span>By Phone</span><span>By Email</span></div>
    <div class="note">Please use this area to tell us more about the client and/or services that may be of interest to you. *</div>
    <div class="field" style="left:224px;top:3481px;width:403px;height:83px"></div>
    <div class="submit">Submit Care Inquiry</div>

    <div class="head sm" style="left:576px;top:2988px">Client Information</div>
    <label class="sm" style="left:576px;top:3030px">Client Name *</label>
    <label class="sm" style="left:785px;top:3032px">Last Name</label>
    <div class="field sm" style="left:576px;top:3059px;width:188px;height:26px">First Name</div>
    <div class="field sm" style="left:785px;top:3059px;width:189px;height:26px">Last Name</div>
    <label class="sm" style="left:576px;top:3096px">First Name</label>
    <label class="sm" style="left:785px;top:3096px">Client Birthdate *</label>
    <div class="field sm" style="left:576px;top:3124px;width:188px;height:26px">First Name</div>
    <div class="field sm c" style="left:785px;top:3124px;width:57px;height:26px">MM</div>
    <div class="field sm c" style="left:848px;top:3124px;width:57px;height:26px">DD</div>
    <div class="field sm c" style="left:910px;top:3124px;width:64px;height:26px">YYYY</div>
    <label class="sm" style="left:576px;top:3169px">Address Where Care Will Be Provided *</label>
    <div class="field" style="left:576px;top:3195px;width:398px;height:26px"></div>
    <label class="sm" style="left:576px;top:3234px">Address 1</label>
    <div class="field" style="left:576px;top:3261px;width:398px;height:26px"></div>
    <label class="sm" style="left:576px;top:3301px">Address 2</label>
    <div class="field" style="left:576px;top:3328px;width:398px;height:26px"></div>
    <label class="sm" style="left:576px;top:3371px">City</label>
    <label class="sm" style="left:675px;top:3371px">State/Province</label>
    <label class="sm" style="left:854px;top:3371px">Zip/Postal Code</label>
    <div class="field" style="left:576px;top:3397px;width:78px;height:27px"></div>
    <div class="field" style="left:675px;top:3397px;width:159px;height:27px"></div>
    <div class="field" style="left:854px;top:3397px;width:120px;height:27px"></div>
  </div>

  <div class="abs footer"></div>
  <div class="social" aria-label="Social links"><span></span><span></span><span></span><span></span><span></span></div>
  <div class="copyright">Copyright 2018 © All rights Reserved</div>

</div>
</body>
</html>
```